Print Design Project- raffle tickets

We need 10 print designs for raffle tickets.
Please create one or two as per specs and do more only if I get in touch with you.
The tickets will be given out to elementary school kids for eating fruits and veggies at lunch time.
The tickets need to bright, colorful and cool.
They will contain the logo (provided), a clip art image (not photo) of a cool teen as per description attached and text. I will need two versions of the final copy- one with the stub and one without the stub for each ticket.
The ticket size is 5.13" by 1.88"
The safe size is 4.92" by 1.67"
The tear off stub is 1" from the right.
The stubs will be a solid color- red, orange, yellow, green and indigo (bluish-purple)
Updates

Target Market(s)

5-12 year olds

Industry/Entity Type

School

Requirements
Must have
• The given text, logo provided and text provided.
The designer will need to put in appropriate clip art pictures of teenagers doing related activities like snowboarding, gardening, basketball etc.
The pictures should look 'cool'. We are trying to make healthy eating be 'cool' and these tickets should be 'wanted' by all the kids in the cafeteria. This should drive them to eat fruits and veggies. High on fun factor.

```html
<!DOCTYPE html>
<html lang="en">
<head>
<meta charset="utf-8">
<title>Raffle Ticket – Raoul</title>
<link rel="stylesheet" href="https://fonts.googleapis.com/css2?family=Reenie+Beanie&display=swap">
<style>
  :root {
    --page: #ffffff;
    --ticket-green: #4cb848;
    --ticket-border: #2b2b2b;
    --stub-indigo: #2e3192;
    --ink-dark: #1e2a1a;
    --ink-name: #2e3192;
    --ink-link: #2a3a9c;
    --art-sticker: #ffffff;
    --art-warm: #f7c72d;
    --art-mid: #e8336d;
    --art-cool: #3f58c9;
  }
  * { margin: 0; padding: 0; box-sizing: border-box; }
  html, body {
    width: 1200px;
    height: 469px;
    overflow: hidden;
    background: var(--page);
  }
  .ticket {
    position: relative;
    width: 1200px;
    height: 469px;
    overflow: hidden;
    font-family: "Reenie Beanie", cursive;
  }
  .ticket-body {
    position: absolute;
    left: 2px;
    top: 25px;
    width: 930px;
    height: 425px;
    background: var(--ticket-green);
    border: 2px solid var(--ticket-border);
  }
  .ticket-stub {
    position: absolute;
    left: 930px;
    top: 18px;
    width: 230px;
    height: 432px;
    background: var(--stub-indigo);
  }
  .brand {
    position: absolute;
    left: 118px;
    top: 232px;
    width: 380px;
    transform: translate(-50%, -50%) rotate(-90deg);
    display: flex;
    align-items: center;
    justify-content: center;
    gap: 12px;
    color: var(--ink-dark);
    font-size: 40px;
    line-height: 44px;
    letter-spacing: 1px;
    white-space: nowrap;
  }
  .brand-mark {
    width: 16px;
    height: 16px;
    border-radius: 50%;
    background: var(--ink-dark);
    flex: none;
  }
  .story {
    position: absolute;
    left: 216px;
    top: 98px;
    color: var(--ink-dark);
    font-size: 38px;
    white-space: nowrap;
  }
  .story-line {
    display: block;
    height: 43px;
    line-height: 43px;
  }
  .story-line--indent { padding-left: 12px; }
  .story-name {
    color: var(--ink-name);
    font-size: 108px;
    line-height: 43px;
  }
  .story-ellipsis {
    color: var(--ink-name);
    font-size: 60px;
    line-height: 43px;
    margin-right: 8px;
  }
  .story-link { color: var(--ink-link); }
  .character-art {
    position: absolute;
    left: 690px;
    top: 40px;
    width: 235px;
    height: 385px;
  }
</style>
</head>
<body>
  <main class="ticket">
    <section class="ticket-body"></section>
    <aside class="ticket-stub" aria-label="Tear-off stub"></aside>

    <div class="brand">
      <span class="brand-mark" aria-hidden="true"></span>
      <span class="brand-name">Color Plate Challenge</span>
    </div>

    <p class="story">
      <span class="story-line"><span class="story-name">Raoul</span> <span class="story-ellipsis">...</span>his favorite sport</span>
      <span class="story-line story-line--indent">is tennis and he's working hard to</span>
      <span class="story-line">be a research scientist. He eats</span>
      <span class="story-line">smart to stay strong; he loves to</span>
      <span class="story-line">munch on kale chips that his</span>
      <span class="story-line">mom makes. Get the recipe at</span>
      <span class="story-line story-link">www.ColorPlateKids.com</span>
    </p>

    <svg class="character-art" viewBox="0 0 235 385" role="img"
         aria-label="Rainbow-outlined illustration of a teen boy leaning on a tennis racket with a tennis ball at his feet">
      <defs>
        <linearGradient id="artRainbow" x1="0" y1="0" x2="0" y2="1">
          <stop offset="0" stop-color="var(--art-warm)" stop-opacity="0.55"/>
          <stop offset="0.5" stop-color="var(--art-mid)" stop-opacity="0.45"/>
          <stop offset="1" stop-color="var(--art-cool)" stop-opacity="0.5"/>
        </linearGradient>
      </defs>
      <path d="M95,6 H197 Q227,6 227,36 V350 Q227,378 197,378 H45 Q12,378 12,350 V238 Q12,208 42,208 H50 Q68,208 68,190 V36 Q68,6 95,6 Z"
            fill="url(#artRainbow)" stroke="var(--art-sticker)" stroke-width="9" stroke-linejoin="round"/>
    </svg>
  </main>
</body>
</html>
```